Real estate Agent postcards for homeowners

I need a "Just Sold" postcard for two real agents , I am providing pictures of the agents and neighborhood.
I have the front and back of a postcard containing the information I want on the postcard.
I want a designer to take the info and pictures and design a new postcard and choose the colors

Target Market(s)

homeowners of luxury condos

Industry/Entity Type

Real Estate Agent

Colors

Designer to choose colors to be used in the design.

```html
<!DOCTYPE html>
<html lang="en">
<head>
<meta charset="utf-8">
<title>Lagunita Realtors – Postcard Back</title>
<link rel="stylesheet" href="https://fonts.googleapis.com/css2?family=Source+Sans+3:wght@400;600;700&family=Tinos:wght@700&display=swap">
<style>
  :root {
    --brand-orange: #D96A45;
    --band-charcoal: #3A3A3C;
    --paper: #FFFFFF;
    --ink: #1E1E1E;
  }
  * { margin: 0; padding: 0; box-sizing: border-box; }
  html, body { width: 1200px; height: 858px; overflow: hidden; background: var(--paper); }
  body { font-family: "Source Sans 3", sans-serif; }
  .postcard { position: relative; width: 1200px; height: 858px; background: var(--paper); }
  .agent-panel {
    position: absolute; left: 0; top: 0; width: 600px; height: 858px;
    background: var(--brand-orange); color: var(--paper); text-align: center;
  }
  .line { position: absolute; left: 0; width: 600px; line-height: 1; white-space: nowrap; }
  .brokerage-name { font-family: "Tinos", serif; font-weight: 700; font-size: 47px; top: 22px; letter-spacing: 0.3px; }
  .brokerage-address { font-size: 23px; top: 69px; }
  .intro-band {
    position: absolute; left: 0; top: 124px; width: 600px; height: 172px;
    background: var(--band-charcoal);
  }
  .intro-text { position: absolute; left: 40px; top: 8px; width: 520px; font-size: 27px; line-height: 28.5px; }
  .intro-line { display: block; white-space: nowrap; text-align: justify; text-align-last: justify; }
  .intro-line--last { text-align: center; text-align-last: center; }
  .visit-label { font-size: 30px; font-weight: 600; top: 101px; }
  .website { font-size: 25px; top: 134px; }
  .agent-name { font-size: 43px; font-weight: 700; letter-spacing: 0.3px; }
  .agent-phone, .agent-email { font-size: 30px; }
  .badge {
    position: absolute; left: 188px; top: 656px; width: 203px; height: 106px;
    background: var(--paper);
  }
  .license { font-size: 32px; top: 800px; }
  .disclaimer {
    position: absolute; left: 629px; top: 780px; width: 547px;
    font-size: 21.5px; line-height: 28.5px; color: var(--ink);
  }
  .disclaimer-line { display: block; white-space: nowrap; text-align: justify; text-align-last: justify; }
  .disclaimer-line--last { text-align: center; text-align-last: center; }
</style>
</head>
<body>
<main class="postcard">
  <section class="agent-panel">
    <h1 class="line brokerage-name">LAGUNITA REALTORS</h1>
    <p class="line brokerage-address">47 Seabreeze Ave Avalon, CA 90704-1100</p>

    <div class="intro-band">
      <p class="intro-text">
        <span class="intro-line">We are Avalon agents and your Hamilton</span>
        <span class="intro-line">Cove Neighbours, Call Us for a free property</span>
        <span class="intro-line intro-line--last">market evaluation.</span>
      </p>
      <p class="line visit-label">Visit Us At</p>
      <p class="line website">www.LagunitaRealtors.com</p>
    </div>

    <h2 class="line agent-name" style="top:335px">MARLA KINSEY</h2>
    <p class="line agent-phone" style="top:387px">(310) 555-0148</p>
    <p class="line agent-email" style="top:421px">HomesbyMarla@mailbox.com</p>

    <h2 class="line agent-name" style="top:492px">THEO VARLAS</h2>
    <p class="line agent-phone" style="top:544px">(650) 555-0192</p>
    <p class="line agent-email" style="top:578px">TheoVarlas@inboxmail.com</p>

    <svg class="badge" viewBox="0 0 203 106" role="img" aria-label="Membership and listing service badge">
      <rect x="5" y="4" width="193" height="98" fill="none" stroke="#1E1E1E" stroke-width="2"/>
      <rect x="14" y="10" width="72" height="68" fill="#1E1E1E"/>
      <rect x="100" y="38" width="88" height="40" fill="none" stroke="#1E1E1E" stroke-width="1.5"/>
    </svg>

    <p class="line license">CALBRE # 00482715</p>
  </section>

  <p class="disclaimer">
    <span class="disclaimer-line">If your property is already listed with a broker please</span>
    <span class="disclaimer-line disclaimer-line--last">disregard this mailing this is not a solicitation</span>
  </p>
</main>
</body>
</html>
```